Consulting and Personal Growth company needs instagram design

Design of Instagram feed.
Please see attached:
1. Design brief with all details and mood board
2. Posts texts
3. Brand logo and colors

Objective:
Design Instagram feed for The Lumen Compass so that the posts flow visually while each post looks beautiful by itself. The posts have the following order:

THEME: 1 PURPOSE - 3 posts
HEALTH - 3 posts
MIND - 3 posts
VISION - 3 posts
Every post will be posted independently (not in groups of 3)
Use @thelumencompass in all posts. (See post texts in attachment)

Target Market(s)

Business owners and executives, men and women who want to maximize their potential and impact.

Industry/Entity Type

Consulting

Font styles to use
Other font styles liked:
• Avenir

Requirements
Must have
• Clean, professional design
• Beautiful flow of posts in feed
• Eye-catching independent posts
• Feed is not disrupted when adding a new post
• Use @thelumencompass in all posts.
Nice to have
• Logo "star" can be used in posts if it helps build branding but not mandatory.
Should not have
• Each post independent with no flow/beautiful design of feed.

```html
<!DOCTYPE html>
<html lang="en">
<head>
<meta charset="utf-8">
<title>The Lumen Compass — Purpose Post</title>
<link rel="stylesheet" href="https://fonts.googleapis.com/css2?family=Nunito+Sans:wght@400;700&display=swap">
<style>
  :root {
    --paper: #ffffff;
    --ink: #111111;
    --accent: #67b8e3;
    --photo-light: #e3eff7;
    --photo-mid: #a9d0ea;
    --photo-deep: #5d9fcd;
  }
  html, body {
    margin: 0;
    padding: 0;
    width: 1200px;
    height: 1200px;
    overflow: hidden;
    background: var(--paper);
  }
  .post {
    position: relative;
    width: 1200px;
    height: 1200px;
    overflow: hidden;
    background: var(--paper);
    font-family: "Nunito Sans", "Avenir", sans-serif;
    color: var(--ink);
  }
  .post__art {
    position: absolute;
    inset: 0;
    width: 1200px;
    height: 1200px;
  }
  .post__quote {
    position: absolute;
    left: 52px;
    top: 46px;
    margin: 0;
    font-size: 62px;
    font-weight: 400;
    line-height: 78px;
    letter-spacing: 0.2px;
    white-space: nowrap;
  }
  .post__highlight {
    color: var(--accent);
    font-weight: 700;
  }
  .post__author {
    position: absolute;
    left: 52px;
    top: 364px;
    margin: 0;
    font-size: 58px;
    font-weight: 400;
    line-height: 1;
    white-space: nowrap;
  }
  .brand {
    position: absolute;
    left: 50px;
    top: 484px;
    display: flex;
    align-items: center;
    gap: 24px;
  }
  .brand__dot {
    width: 124px;
    height: 124px;
    border-radius: 50%;
    background: var(--accent);
  }
  .brand__name {
    margin: 0;
    font-size: 26px;
    font-weight: 400;
    letter-spacing: 6px;
    text-transform: uppercase;
    line-height: 38px;
    color: var(--ink);
  }
  .post__handle {
    position: absolute;
    left: 52px;
    top: 648px;
    margin: 0;
    font-size: 30px;
    font-weight: 400;
    line-height: 1;
    color: var(--ink);
    white-space: nowrap;
  }
</style>
</head>
<body>
  <main class="post">
    <svg class="post__art" viewBox="0 0 1200 1200">
      <defs>
        <linearGradient id="photoTone" x1="1" y1="0" x2="0.3" y2="1">
          <stop offset="0" stop-color="#e3eff7"/>
          <stop offset="0.5" stop-color="#a9d0ea"/>
          <stop offset="1" stop-color="#5d9fcd"/>
        </linearGradient>
      </defs>
      <polygon role="img" aria-label="Photo of athletes running through the water jump of a steeplechase race in a stadium"
               points="1200,0 1200,1200 0,1200" fill="url(#photoTone)"/>
      <polygon class="post__band" points="1160,0 1205,0 5,1200 -40,1200" fill="#67b8e3"/>
    </svg>

    <p class="post__quote">
      When you are <span class="post__highlight">PURPOSE-driven</span><br>
      you live a fulfilling life and you<br>
      are true to yourself.
    </p>

    <p class="post__author">Mara Delcourt</p>

    <div class="brand">
      <div class="brand__dot"></div>
      <p class="brand__name">The<br>Lumen<br>Compass</p>
    </div>

    <p class="post__handle">@thelumencompass</p>
  </main>
</body>
</html>
```